plumbing & gas fitting business card design

We need a business card design for a plumbing & gas fitting company. The company covers commercial, domestic and maintenance work. We would like a modern design communicating efficiency and sophistication. preferred colours would include (red grey & black) or (green grey & black). Please DO NOT include any water droplets.

Varcoe Plumbing & Gas, Commercial Domestic & Maintenance, licence no. 418736K, ABN 57204918362, Phone 0417382965, Email varcoeplumbingandgas@tidemail.com

```html
<!DOCTYPE html>
<html lang="en">
<head>
<meta charset="utf-8">
<title>Varcoe Plumbing &amp; Gas – Business Card</title>
<link rel="stylesheet" href="https://fonts.googleapis.com/css2?family=Barlow:wght@400;500;600;700&display=swap">
<style>
  :root {
    --page: #f1f1f2;
    --card-grey: #c9cacc;
    --card-white: #ffffff;
    --panel-grey: #77787b;
    --brand-red: #c0393b;
    --ink-dark: #231f20;
    --ink-muted: #6d6e71;
    --card-black: #191516;
    --white: #ffffff;
  }
  * { box-sizing: border-box; margin: 0; padding: 0; }
  html, body {
    width: 985px;
    height: 1200px;
    overflow: hidden;
    background: var(--page);
    font-family: "Barlow", sans-serif;
  }
  .card {
    position: absolute;
    left: 137px;
    width: 663px;
    height: 370px;
    overflow: hidden;
  }
  .card--front { top: 153px; background: var(--card-grey); }
  .card--back  { top: 664px; background: var(--card-black); }

  .brand {
    position: absolute;
    left: 0;
    right: 0;
    text-align: center;
    font-weight: 700;
    line-height: 1;
  }
  .brand__mark {
    display: block;
    width: 58px;
    height: 58px;
    margin: 0 auto 18px;
    background: var(--brand-red);
    border-radius: 8px;
  }
  .brand__name {
    display: block;
    font-size: 50px;
    letter-spacing: 2px;
  }
  .brand__trade {
    display: block;
    font-size: 27px;
    letter-spacing: 1.5px;
    margin-top: 2px;
  }
  .card--front .brand { top: 60px; color: var(--ink-dark); }
  .card--back  .brand { top: 60px; color: var(--white); }

  .front__base {
    position: absolute;
    left: 0; right: 0; bottom: 0;
    top: 291px;
    background: var(--card-white);
  }
  .front__rule {
    position: absolute;
    left: 0; right: 0;
    top: 288px;
    height: 6px;
    background: var(--brand-red);
  }
  .contact-panel {
    position: absolute;
    left: 77px;
    top: 260px;
    width: 504px;
    height: 66px;
    background: var(--panel-grey);
    border-radius: 0 24px 0 24px;
    color: var(--white);
    text-align: center;
    padding-top: 7px;
  }
  .contact-panel__phone {
    font-size: 23px;
    font-weight: 600;
    line-height: 27px;
  }
  .contact-panel__email {
    font-size: 17px;
    font-weight: 400;
    line-height: 24px;
  }
  .front__registration {
    position: absolute;
    left: 0; right: 0;
    top: 333px;
    text-align: center;
    font-size: 15px;
    color: var(--ink-muted);
  }

  .services-panel {
    position: absolute;
    left: 81px;
    top: 272px;
    width: 513px;
    height: 69px;
    background: var(--brand-red);
    border-radius: 0 24px 0 24px;
    color: var(--white);
    text-align: center;
    font-size: 20px;
    font-weight: 500;
    letter-spacing: 0.6px;
    line-height: 26px;
    padding-top: 9px;
    text-transform: uppercase;
  }
</style>
</head>
<body>
  <section class="card card--front" aria-label="Business card front">
    <div class="brand">
      <span class="brand__mark"></span>
      <span class="brand__name">VARCOE</span>
      <span class="brand__trade">PLUMBING &amp; GAS</span>
    </div>
    <div class="front__base"></div>
    <div class="front__rule"></div>
    <div class="contact-panel">
      <p class="contact-panel__phone">Ph: 04 1738 2965</p>
      <p class="contact-panel__email">E: varcoeplumbingandgas@tidemail.com</p>
    </div>
    <p class="front__registration">Licence No. 418736K&nbsp; ABN 57204918362</p>
  </section>

  <section class="card card--back" aria-label="Business card back">
    <div class="brand">
      <span class="brand__mark"></span>
      <span class="brand__name">VARCOE</span>
      <span class="brand__trade">PLUMBING &amp; GAS</span>
    </div>
    <div class="services-panel">
      <p>Plumbing, Gas Fitting,</p>
      <p>Commercial, Domestic &amp; Maintenance</p>
    </div>
  </section>
</body>
</html>
```